Resinex Pro color chart design

We are in need to have a color chart (pdf to be displayed on our website-www.resinexpro-sample.com as well as for print) to show customers what their color choices are for our metallic epoxy pigments. We would like it to be modern amd clean. A white background will allow the color swatches to stand out. our company colors are orange, grey and white. Looking for the color swatches to be as large as possible while still being able to display our logo, contact info and disclaimers. We are open to any design ideas. If needed it can be put on two pages.

Additional info to add: Resinex Pro Shimmer Tint Powders are special effect pigments composed of mica nano-particles coated with various organic and inorganic pigments to create pearlescent and iridescent effects that mimic the
natural look of stone and rock formations. These unique pigments are designed to be field blended with Resinex Pro Artisan Lustre clear epoxy. When the metallic particles are mixed with our epoxy they give the coating a shine that reflects light and creates an eye-catching dramatic color. For the most vivid color and dynamic effects we recommend (1) 16oz jar of metallic pigment for each 3 Gallon kit of our Artisan Lustre Epoxy.

Disclaimer: The colors on this chart are represented as closely as possible. Variations should be expected due to differences in substrate conditions, thickness of application, speed of curing, blending of colors, application technique, color of initial primer coat and screen resolution. For additional information and application instructions visit www.resinexpro-sample.com

Contact info: Tel. 1-800-555-0147
www.resinexpro-sample.com

Target Market(s)

Online. This will be a link on our website

Font styles to use
Sans Serif

Colors
f37122
5c5c5c
ffffff

Requirements
Must have
• A white background will allow the color swatches to stand out. Disclaimer should be in small print but still readable.
Nice to have
• Can use our company colors as part of the design
Should not have
• Should not look and feel cluttered.

```html
<!DOCTYPE html>
<html lang="en">
<head>
<meta charset="utf-8">
<title>Resinex Pro – Metallic Epoxy Pigments Color Chart</title>
<link href="https://fonts.googleapis.com/css2?family=Open+Sans:wght@400;600;700&family=Oswald:wght@400;500&display=swap" rel="stylesheet">
<style>
  :root {
    --brand-orange: #f37122;
    --deco-orange: rgba(232, 103, 58, 0.85);
    --deco-grey: rgba(110, 110, 110, 0.55);
    --ink: #5c5c5c;
    --ink-soft: #6a6a6a;
    --paper: #ffffff;
    --backdrop: #f2f2f2;
    --rule: #8a8a8a;
  }
  * { margin: 0; padding: 0; box-sizing: border-box; }
  html, body { width: 1200px; height: 1200px; overflow: hidden; background: var(--backdrop); }
  .sheet {
    position: absolute; left: 220px; top: 30px;
    width: 760px; height: 1140px;
    background: var(--paper); overflow: hidden;
    font-family: "Open Sans", sans-serif; color: var(--ink);
  }
  .corner-accent { position: absolute; }
  .corner-accent--top-left {
    left: 0; top: 0; width: 140px; height: 120px;
    background: radial-gradient(ellipse at 0 0, var(--deco-orange) 0%, var(--deco-grey) 45%, transparent 72%);
  }
  .corner-accent--top-right {
    right: 0; top: 0; width: 320px; height: 150px;
    background: radial-gradient(ellipse at 100% 0, var(--deco-orange) 0%, var(--deco-orange) 25%, var(--deco-grey) 50%, transparent 72%);
  }
  .corner-accent--bottom-left {
    left: 0; bottom: 0; width: 230px; height: 170px;
    background: radial-gradient(ellipse at 0 100%, var(--deco-orange) 0%, var(--deco-orange) 25%, var(--deco-grey) 52%, transparent 74%);
  }
  .corner-accent--bottom-right {
    right: 0; bottom: 0; width: 140px; height: 70px;
    background: radial-gradient(ellipse at 100% 100%, var(--deco-orange) 0%, var(--deco-grey) 45%, transparent 72%);
  }
  .brand { position: absolute; left: 62px; top: 130px; display: flex; align-items: center; gap: 16px; }
  .brand-mark { width: 64px; height: 64px; border-radius: 50%; background: var(--brand-orange); flex: none; }
  .brand-name { font-size: 38px; font-weight: 600; color: var(--brand-orange); line-height: 1; letter-spacing: -0.5px; }
  .brand-tagline { font-size: 10px; color: var(--ink); margin-top: 5px; }
  .chart-title {
    position: absolute; left: 64px; top: 234px;
    border-left: 2px solid var(--ink); padding-left: 14px;
    font-family: "Oswald", sans-serif; font-weight: 500; font-size: 25px; line-height: 26px;
    color: var(--ink); text-transform: uppercase;
  }
  .intro {
    position: absolute; left: 62px; top: 306px; width: 293px;
    font-size: 16.6px; line-height: 23.6px; text-align: justify; hyphens: auto;
    color: var(--ink-soft);
  }
  .disclaimer {
    position: absolute; left: 62px; top: 790px; width: 293px;
    font-size: 12.6px; line-height: 18.2px; text-align: justify; hyphens: auto; color: var(--ink-soft);
  }
  .disclaimer strong { font-weight: 700; color: var(--ink); }
  .contact {
    position: absolute; left: 62px; top: 977px; width: 293px;
    text-align: center; font-size: 13px; font-weight: 700; line-height: 17px; color: var(--ink);
  }
  .divider { position: absolute; left: 386px; top: 136px; width: 1px; height: 926px; background: var(--rule); }
  .swatch { position: absolute; width: 88px; text-align: center; }
  .swatch-chip {
    display: block; margin: 0 auto; width: 69px; height: 69px;
    background: var(--paper); padding: 3px;
    box-shadow: 0 1px 3px rgba(0,0,0,0.25);
  }
  .swatch-chip span { display: block; width: 100%; height: 100%; }
  .swatch-name {
    display: block; margin-top: 11px;
    font-family: "Oswald", sans-serif; font-size: 12px; letter-spacing: 0.2px;
    color: var(--ink); text-transform: uppercase;
  }
</style>
</head>
<body>
<main class="sheet">
  <div class="corner-accent corner-accent--top-left" role="img" aria-label="Decorative orange and grey geometric corner accent"></div>
  <div class="corner-accent corner-accent--top-right" role="img" aria-label="Decorative orange and grey geometric corner accent"></div>
  <div class="corner-accent corner-accent--bottom-left" role="img" aria-label="Decorative orange and grey geometric corner accent"></div>
  <div class="corner-accent corner-accent--bottom-right" role="img" aria-label="Decorative orange and grey geometric corner accent"></div>

  <header class="brand">
    <span class="brand-mark"></span>
    <div>
      <div class="brand-name">Resinex Pro</div>
      <div class="brand-tagline">Resin coatings and a whole lot more.</div>
    </div>
  </header>

  <h1 class="chart-title">Metalic Epoxy Pigments<br>Color Chart</h1>

  <p class="intro">Resinex Pro Shimmer Tint Powders are special effect pigments composed of mica nano-particles coated with various organic and inorganic pigments to create pearlescent and iridescent effects that mimic the natural look of stone and rock formations. These unique pigments are designed to be field blended with Resinex Pro Artisan Lustre clear epoxy. When the metallic particles are mixed with our epoxy they give the coating a shine that reflects light and creates an eye-catching dramatic color. For the most vivid color and dynamic effects we recommend (1) 16oz jar of metallic pigment for each 3 Gallon kit of our Artisan Lustre Epoxy.</p>

  <p class="disclaimer"><strong>Disclaimer</strong>: The colors on this chart are represented as closely as possible. Variations should be expected due to differences in substrate conditions, thickness of application, speed of curing, blending of colors, application technique, color of initial primer coat and screen resolution. For additional information and application instructions visit www.resinexpro-sample.com.</p>

  <p class="contact">Contact: Tel. 1-800-555-0147<br>www.resinexpro-sample.com</p>

  <div class="divider"></div>

  <section class="swatches">
    <div class="swatch" style="left:442px;top:132px"><span class="swatch-chip"><span style="background:linear-gradient(135deg,#c4622a,#b0531f)"></span></span><span class="swatch-name">Brass</span></div>
    <div class="swatch" style="left:530px;top:132px"><span class="swatch-chip"><span style="background:#b31c42"></span></span><span class="swatch-name">Bubblegum</span></div>
    <div class="swatch" style="left:618px;top:132px"><span class="swatch-chip"><span style="background:linear-gradient(135deg,#e3962a,#d98a1f)"></span></span><span class="swatch-name">Cairo</span></div>

    <div class="swatch" style="left:442px;top:252px"><span class="swatch-chip"><span style="background:#f2b21c"></span></span><span class="swatch-name">Canary</span></div>
    <div class="swatch" style="left:530px;top:252px"><span class="swatch-chip"><span style="background:linear-gradient(135deg,#7a2412,#8a2e18)"></span></span><span class="swatch-name">Cinnamon</span></div>
    <div class="swatch" style="left:618px;top:252px"><span class="swatch-chip"><span style="background:#2d1a0e"></span></span><span class="swatch-name">Coffee</span></div>

    <div class="swatch" style="left:442px;top:372px"><span class="swatch-chip"><span style="background:linear-gradient(135deg,#b8381c,#a5311a)"></span></span><span class="swatch-name">Copper</span></div>
    <div class="swatch" style="left:530px;top:372px"><span class="swatch-chip"><span style="background:linear-gradient(135deg,#c9c9c9,#e2e2e2)"></span></span><span class="swatch-name">Diamond</span></div>
    <div class="swatch" style="left:618px;top:372px"><span class="swatch-chip"><span style="background:#194d37"></span></span><span class="swatch-name">Forest Green</span></div>

    <div class="swatch" style="left:442px;top:492px"><span class="swatch-chip"><span style="background:#2a1c6a"></span></span><span class="swatch-name">Grape</span></div>
    <div class="swatch" style="left:530px;top:492px"><span class="swatch-chip"><span style="background:linear-gradient(135deg,#25432a,#2f4f30)"></span></span><span class="swatch-name">Green Apple</span></div>
    <div class="swatch" style="left:618px;top:492px"><span class="swatch-chip"><span style="background:#121214"></span></span><span class="swatch-name">Gunmetal</span></div>

    <div class="swatch" style="left:442px;top:601px"><span class="swatch-chip"><span style="background:linear-gradient(135deg,#6a3c9a,#7d4aa8)"></span></span><span class="swatch-name">Lilac</span></div>
    <div class="swatch" style="left:530px;top:601px"><span class="swatch-chip"><span style="background:linear-gradient(135deg,#163c9a,#2b64c9,#163c9a)"></span></span><span class="swatch-name">Ocean Blue</span></div>
    <div class="swatch" style="left:618px;top:601px"><span class="swatch-chip"><span style="background:#9a8530"></span></span><span class="swatch-name">Olive Yellow</span></div>

    <div class="swatch" style="left:442px;top:721px"><span class="swatch-chip"><span style="background:linear-gradient(135deg,#c86a26,#c4621f)"></span></span><span class="swatch-name">Orange Gold</span></div>
    <div class="swatch" style="left:530px;top:721px"><span class="swatch-chip"><span style="background:#ebdcd3"></span></span><span class="swatch-name">Pearl</span></div>
    <div class="swatch" style="left:618px;top:721px"><span class="swatch-chip"><span style="background:linear-gradient(135deg,#5a2410,#7a3814)"></span></span><span class="swatch-name">Penny</span></div>

    <div class="swatch" style="left:442px;top:841px"><span class="swatch-chip"><span style="background:#0a9678"></span></span><span class="swatch-name">Sea Green</span></div>
    <div class="swatch" style="left:530px;top:841px"><span class="swatch-chip"><span style="background:linear-gradient(135deg,#6e6466,#7d7576)"></span></span><span class="swatch-name">Silver</span></div>
    <div class="swatch" style="left:618px;top:841px"><span class="swatch-chip"><span style="background:#0c7894"></span></span><span class="swatch-name">Skyblue</span></div>

    <div class="swatch" style="left:442px;top:964px"><span class="swatch-chip"><span style="background:#ee5a22"></span></span><span class="swatch-name">Tangerine</span></div>
    <div class="swatch" style="left:530px;top:964px"><span class="swatch-chip"><span style="background:linear-gradient(135deg,#444042,#2e2c2d)"></span></span><span class="swatch-name">Titanium</span></div>
    <div class="swatch" style="left:618px;top:964px"><span class="swatch-chip"><span style="background:#6a0f10"></span></span><span class="swatch-name">Wine Red</span></div>
  </section>
</main>
</body>
</html>
```